Glintora Rex (GLRX) – Official Website & Presale Landing Page

Glintora Rex (GLRX) is a meme-inspired crypto project built on Veltris, designed to allow users to mine tokens directly from their mobile phones. Our mission is to bring crypto mining to everyone in a simple, fun, and viral way – powered by community engagement, humor, and innovation.

The project combines the simplicity of mobile mining with the viral potential of meme culture. Unlike traditional mining, Glintora Rex does not require expensive equipment or complex setups. Instead, users participate directly from their smartphones, making the project accessible to millions of young investors worldwide.

The landing page will be the central hub for our community. It must be modern, responsive, and visually striking. Key sections should include: Hero section with call-to-action, Tokenomics, Roadmap, Miner Counter ("12,438 Miners and Counting"), Airdrop countdown, App preview, Social media links (Chatvane, Q/Blurbly, Corvel Wallet), and Contact information. We also want a dedicated section for Presale where investors can join directly once the presale goes live.

Nice-to-have features include animated counters, interactive roadmap, video embedding, newsletter signup, global map of miners, dark mode toggle, and a multilingual setup (English, Vietnamese, Chinese, French, German, Slovak). The style should be futuristic, colorful, and engaging – with neon tones and crypto/meme vibes.

The target market is young crypto investors, meme communities, and global users looking for new opportunities in Web3. Our ultimate goal is to grow rapidly, build strong hype, and raise $7M+ during the presale.

The website should reflect excitement, simplicity, and trustworthiness while staying true to meme culture. It must balance professional design with playful elements, creating an experience that keeps users engaged and excited to be part of Glintora Rex.

Target Market(s)

Young crypto investors, meme community, people interested in mobile mining (18–35 years).

Industry/Entity Type

Cryptocurrency / Blockchain / Technology

Coding

Coded - Design and coding required

Number of Pages Required

5+ page

Font styles to use
Sans Serif

Colors
A7469A
B969AE
D3A5CF
EDDBEB
F8F0F9
6B429C
8869AF
B7A5CE
E3DAEB
F3F0F8

Requirements
Must have
• Must Haves: - Responsive landing page with sections: Hero (headline, subheadline, CTA button), Tokenomics, Total Supply, Roadmap, Airdrop, App, Team/Founder, Contact, Social links (X, Chatvane, Email). - Additional dedicated Presale Landing Page (1 page) with: - Hero headline (Join the $GLRX Presale – Mine Crypto From Your Phone!) + CTA button (Buy GLRX Now). - Countdown timer for presale phase. - Presale phases (3 phases) with price and allocation: - Phase 1 – Private Sale: $0.005, 100M GLRX - Phase 2 – Public Sale: $0.01, 150M GLRX - Phase 3 – Final Sale: $0.02, 100M GLRX - Total presale allocation: 350M GLRX (35% of supply). - “How to Participate” steps (Connect wallet → Select amount → Confirm transaction → Claim tokens). - Claim system placeholder (button). - Security & trust badges: verified contract on Ledgrove, transparent tokenomics, locked liquidity. - Fully modern, clean, crypto-style design with bold colors (purple + dark + neon contrasts). - Clear CTA buttons (Buy, Join Airdrop, Connect Wallet). - Mobile-friendly (responsive) design.
Nice to have
• Animated counters (e.g., "12,438 Miners and Counting"). - Interactive roadmap with hover/scroll reveal. - Language switcher (at least 5–7 languages: English, Vietnamese, Chinese, French, German, Slovak). - Embedded promo video (Clipnest/Reelo). - Newsletter signup (email capture / Postwren). - Global miners map (optional). - Countdown timers for presale and airdrop. - Light parallax/particle background (neon/futuristic). - Dark mode toggle (optional). - Simple CMS-friendly structure (easy to add blog/updates later).
Should not have
• Too formal corporate style, long boring text, outdated templates.

```html
<!DOCTYPE html>
<html lang="en">
<head>
<meta charset="utf-8">
<title>Glintora Rex (GLRX) – Mine Crypto From Your Phone</title>
<link rel="stylesheet" href="https://fonts.googleapis.com/css2?family=Roboto:wght@400;500;600;700;800&display=swap">
<style>
:root{
  --bg:#120a3c;
  --bg-deep:#0c0630;
  --panel:#1f0d5e;
  --panel-2:#2a1275;
  --violet:#6b429c;
  --violet-2:#8869af;
  --lilac:#b7a5ce;
  --lilac-soft:#e3daeb;
  --pink:#a7469a;
  --pink-2:#b969ae;
  --pink-soft:#d3a5cf;
  --white:#ffffff;
  --orange:#f08a24;
  --neon:#8b3cff;
  --btn:#e3d3fb;
}
*{margin:0;padding:0;box-sizing:border-box}
html,body{width:1200px;height:5277px;overflow:hidden}
body{position:relative;background:var(--bg);color:var(--white);font-family:"Roboto",sans-serif}
.abs{position:absolute}
a{color:inherit;text-decoration:none}

/* backgrounds & illustration areas */
.bg-hero{left:0;top:0;width:1200px;height:640px;background:radial-gradient(ellipse at 30% 60%,#2d1a7a 0%,#1a0f52 45%,var(--bg) 100%)}
.art-hero{left:640px;top:110px;width:430px;height:445px;border-radius:24px;background:radial-gradient(circle at 50% 45%,#f2b640 0%,#b3572f 35%,#3a1d6e 75%,transparent 100%)}
.art-miner{left:0;top:1600px;width:1200px;height:660px;background:radial-gradient(ellipse at 62% 42%,#8c5a34 0%,#4a2e55 28%,#231458 55%,var(--bg) 85%)}
.art-platform{left:280px;top:3400px;width:640px;height:170px;background:radial-gradient(ellipse at 50% 60%,#2ee6ff 0%,#2a3ca8 35%,#1a1260 70%,transparent 100%)}
.art-phone{left:700px;top:3730px;width:400px;height:560px;background:radial-gradient(ellipse at 50% 50%,#f5c542 0%,#6a3cc0 35%,#2a1478 65%,transparent 100%)}

/* header */
.logo{display:flex;align-items:center;gap:10px}
.logo-dot{width:52px;height:52px;border-radius:50%;background:var(--white)}
.logo-name{font-weight:700;line-height:1}
.logo-name small{display:block;font-size:12px;font-weight:500}
.logo-name b{display:block;font-size:24px;font-weight:800;margin-top:2px}
.nav{left:330px;top:58px;display:flex;gap:16px;font-size:12px}
.nav a.active{font-weight:700}
.socials{display:flex;gap:10px;align-items:center;font-size:12px;font-weight:500}
.socials span{display:flex;align-items:center;gap:5px;white-space:nowrap}
.socials i{width:10px;height:10px;border-radius:50%;background:var(--white);display:block}
.socials.top{left:866px;top:58px;font-size:10px;gap:8px}
.socials.top i{width:8px;height:8px}
.lang{display:flex;align-items:center;gap:6px;font-size:13px}
.lang i{width:18px;height:18px;border-radius:50%;background:var(--lilac-soft);display:block}

.btn{display:inline-flex;align-items:center;justify-content:center;background:var(--btn);color:#2a1070;font-weight:600;border-radius:20px;box-shadow:0 0 0 3px #8b3cff,0 0 14px #8b3cff}

.hero-title{left:152px;top:182px;font-size:46px;line-height:56px;font-weight:500}
.hero-title b{font-weight:700}
.hero-sub{left:152px;top:312px;width:360px;font-size:13px;line-height:20px}

/* panels */
.panel{border-radius:10px}
.counter-box{left:148px;top:682px;width:903px;height:303px;background:linear-gradient(180deg,#2a2570 0%,#1a1156 100%)}
.sec-title{width:100%;text-align:center;font-weight:700}
.digit{width:106px;height:102px;border:2px solid #cbb6ff;border-radius:16px;background:#150b45;display:flex;align-items:center;justify-content:center;font-size:38px;font-weight:700}
.colon{font-size:34px;font-weight:700}

.legend{left:709px;width:342px;height:66px;background:#2b1070;border-radius:6px;border-left:4px solid var(--orange);display:flex;align-items:center;padding-left:22px;font-size:16px;font-weight:500}
.legend.alt{border-left-color:#a45cff}
.legend b{font-size:28px;font-weight:600;margin-right:8px}

.rm-circle{width:88px;height:88px;border-radius:50%;border:2px solid #9a4dff;background:#1c0b52;display:flex;align-items:center;justify-content:center;font-size:32px;font-weight:500}
.rm-dot{width:14px;height:14px;border-radius:50%;background:#f3c8ff;box-shadow:0 0 8px #f3c8ff}
.rm-label{width:160px;text-align:center;font-size:13px;line-height:18px}
.rm-label b{display:block;font-size:16px;font-weight:700}
.rm-dash{width:0;border-left:2px dashed #a45cff}

.glow-box{border-radius:28px;background:linear-gradient(180deg,#2a0f73 0%,#1d0a56 100%);box-shadow:0 0 0 3px #7a2ee0,0 0 30px #7a2ee0}
.timer-cell{width:106px;height:104px;border:2px solid #cbb6ff;border-radius:14px;background:#14093d;display:flex;align-items:center;justify-content:center;font-size:40px;font-weight:500}
.timer-label{width:106px;text-align:center;font-size:13px;font-weight:600}

.app-title{left:150px;top:4014px;font-size:43px;line-height:56px;font-weight:700}

.foot-col h4{font-size:15px;font-weight:600;margin-bottom:20px}
.foot-col a{display:block;font-size:12px;margin-bottom:14px}
.contact-row{display:flex;gap:14px;font-size:12px;line-height:17px;margin-bottom:22px}
.contact-row svg{flex:none}
</style>
</head>
<body>

<!-- Background illustration areas (behind content) -->
<div class="abs bg-hero" role="img" aria-label="Dark purple digital mining landscape backdrop"></div>
<div class="abs art-hero" role="img" aria-label="Mascot illustration: miner with pickaxe holding a phone, with Glintora Rex title lettering"></div>
<div class="abs art-miner" role="img" aria-label="Illustration of a miner digging out a giant glowing crypto coin from rock"></div>

<header>
  <a class="abs logo" style="left:150px;top:14px">
    <span class="logo-dot"></span>
    <span class="logo-name"><small>Glintora Rex</small><b>GLRX</b></span>
  </a>
  <div class="abs lang" style="left:944px;top:17px"><i></i>English
    <svg width="9" height="6" viewBox="0 0 9 6"><path d="M1 1l3.5 3.5L8 1" stroke="#fff" fill="none" stroke-width="1.4"/></svg></div>
  <nav class="abs nav">
    <a class="active">Home</a><a>Tokenomics</a><a>Total Supply</a><a>Roadmap</a><a>Airdrop App</a><a>Team/Founder</a><a>Contact</a>
  </nav>
  <div class="abs socials top">
    <span><i></i>Chatvane</span><span><i></i>Q/Blurbly</span><span><i></i>Corvel Wallet</span>
  </div>
</header>

<section>
  <h1 class="abs hero-title">Mine Crypto<br><b>From Your Phone</b></h1>
  <p class="abs hero-sub">Glintora Rex (GLRX) brings mining to everyone – simple, fun, and viral.</p>
  <a class="abs btn" style="left:152px;top:389px;width:146px;height:34px;font-size:13px">Join Presale</a>
</section>

<!-- Miners counter -->
<section class="abs counter-box panel">
  <h2 class="sec-title" style="margin-top:34px;font-size:38px">12,438 Miners and Counting</h2>
  <svg class="abs" style="left:575px;top:87px" width="120" height="14" viewBox="0 0 120 14"><path d="M4 10 Q60 0 116 6" stroke="var(--orange)" stroke-width="4" fill="none" stroke-linecap="round"/></svg>
  <div class="abs" style="left:53px;top:138px;display:flex;align-items:center;gap:22px">
    <div class="digit">1</div><span class="colon">:</span>
    <div class="digit">2</div><span class="colon">:</span>
    <div class="digit">4</div><span class="colon">:</span>
    <div class="digit">3</div><span class="colon">:</span>
    <div class="digit">8</div>
  </div>
</section>

<!-- Tokenomics -->
<section>
  <h2 class="abs sec-title" style="top:1068px;font-size:42px">Tokenomics</h2>
  <svg class="abs" style="left:540px;top:1120px" width="120" height="14" viewBox="0 0 120 14"><path d="M4 10 Q60 0 116 6" stroke="var(--orange)" stroke-width="4" fill="none" stroke-linecap="round"/></svg>

  <svg class="abs" style="left:140px;top:1190px" width="520" height="400" viewBox="-250 -200 520 400" font-family="Roboto,sans-serif" fill="#fff">
    <path d="M0 0 L0 -180 A180 180 0 0 1 142.9 -109.5Z" fill="#9b5de5"/>
    <path d="M0 0 L142.9 -109.5 A180 180 0 0 1 180 0Z" fill="#5a17c0"/>
    <path d="M0 0 L180 0 A180 180 0 0 1 105.8 145.6Z" fill="#4a0fa8"/>
    <path d="M0 0 L105.8 145.6 A180 180 0 0 1 -145.6 105.8Z" fill="#7a2ee0"/>
    <path d="M0 0 L-145.6 105.8 A180 180 0 0 1 0 -180Z" fill="#b07ef0"/>
    <g stroke="#fff" stroke-width="3" fill="none">
      <path d="M0 0L0 -180M0 0L142.9 -109.5M0 0L180 0M0 0L105.8 145.6M0 0L-145.6 105.8"/>
    </g>
    <g font-size="18" font-weight="500" text-anchor="middle">
      <text x="50" y="-95">14.6%</text>
      <text x="112" y="-30">10.4%</text>
      <text x="105" y="65">15.0%</text>
      <text x="-16" y="110">25.0%</text>
      <text x="-85" y="-5">35.0%</text>
    </g>
    <g font-size="18">
      <text x="98" y="-165">Reserve</text>
      <text x="190" y="-45">Team</text>
      <text x="158" y="108">Marketing</text>
      <text x="-165" y="175">Liquidity</text>
      <text x="-248" y="-78">Presale</text>
    </g>
  </svg>

  <div class="abs legend" style="top:1200px"><b>35%</b>Presale (350M GLRX)</div>
  <div class="abs legend alt" style="top:1278px"><b>20%</b>Liquidity &amp; MM (200M)</div>
  <div class="abs legend alt" style="top:1356px"><b>15%</b>Airdrop/Community (150M)</div>
  <div class="abs legend" style="top:1434px"><b>15%</b>Team (Locked)</div>
  <div class="abs legend" style="top:1512px"><b>15%</b>Ecosystem/Growth</div>
</section>

<!-- Roadmap -->
<section>
  <h2 class="abs sec-title" style="top:2302px;font-size:42px">Our Roadmap</h2>
  <svg class="abs" style="left:590px;top:2354px" width="120" height="14" viewBox="0 0 120 14"><path d="M4 10 Q60 0 116 6" stroke="var(--orange)" stroke-width="4" fill="none" stroke-linecap="round"/></svg>
  <div class="abs" style="left:150px;top:2677px;width:900px;height:1px;background:#4a2e9a"></div>

  <div class="abs rm-circle" style="left:151px;top:2436px">01</div>
  <div class="abs rm-dash" style="left:195px;top:2526px;height:90px"></div>
  <div class="abs rm-dot" style="left:188px;top:2613px"></div>
  <div class="abs rm-label" style="left:115px;top:2642px">January, 2018<b>Planning</b></div>

  <div class="abs rm-label" style="left:285px;top:2548px">January, 2018<b>Planning</b></div>
  <div class="abs rm-dot" style="left:358px;top:2613px"></div>
  <div class="abs rm-dash" style="left:365px;top:2630px;height:82px"></div>
  <div class="abs rm-circle" style="left:321px;top:2713px">02</div>

  <div class="abs rm-circle" style="left:470px;top:2436px">03</div>
  <div class="abs rm-dash" style="left:514px;top:2526px;height:90px"></div>
  <div class="abs rm-dot" style="left:507px;top:2613px"></div>
  <div class="abs rm-label" style="left:434px;top:2642px">January, 2018<b>Planning</b></div>

  <div class="abs rm-label" style="left:604px;top:2548px">January, 2018<b>Planning</b></div>
  <div class="abs rm-dot" style="left:677px;top:2613px"></div>
  <div class="abs rm-dash" style="left:684px;top:2630px;height:82px"></div>
  <div class="abs rm-circle" style="left:640px;top:2713px">04</div>

  <div class="abs rm-circle" style="left:788px;top:2436px">05</div>
  <div class="abs rm-dash" style="left:832px;top:2526px;height:90px"></div>
  <div class="abs rm-dot" style="left:825px;top:2613px"></div>
  <div class="abs rm-label" style="left:752px;top:2642px">January, 2018<b>Planning</b></div>

  <div class="abs rm-label" style="left:921px;top:2548px">January, 2018<b>Planning</b></div>
  <div class="abs rm-dot" style="left:994px;top:2613px"></div>
  <div class="abs rm-dash" style="left:1001px;top:2630px;height:82px"></div>
  <div class="abs rm-circle" style="left:957px;top:2713px">06</div>
</section>

<!-- Airdrop countdown -->
<section>
  <div class="abs glow-box" style="left:148px;top:3006px;width:903px;height:384px"></div>
  <h2 class="abs sec-title" style="top:3064px;font-size:38px">Countdown Timer</h2>
  <svg class="abs" style="left:540px;top:3112px" width="120" height="14" viewBox="0 0 120 14"><path d="M4 10 Q60 0 116 6" stroke="var(--orange)" stroke-width="4" fill="none" stroke-linecap="round"/></svg>

  <div class="abs timer-cell" style="left:291px;top:3170px">01</div>
  <div class="abs timer-cell" style="left:462px;top:3170px">16</div>
  <div class="abs timer-cell" style="left:633px;top:3170px">02</div>
  <div class="abs timer-cell" style="left:803px;top:3170px">55</div>
  <span class="abs colon" style="left:414px;top:3196px">:</span>
  <span class="abs colon" style="left:585px;top:3196px">:</span>
  <span class="abs colon" style="left:756px;top:3196px">:</span>
  <div class="abs timer-label" style="left:291px;top:3294px">Days</div>
  <div class="abs timer-label" style="left:462px;top:3294px">Hours</div>
  <div class="abs timer-label" style="left:633px;top:3294px">Minutes</div>
  <div class="abs timer-label" style="left:803px;top:3294px">Seconds</div>

  <div class="abs art-platform" role="img" aria-label="Glowing circuit platform with a holographic crypto coin"></div>

  <p class="abs sec-title" style="top:3620px;font-size:28px;font-weight:400">Join our global airdrop before the timer ends!</p>
  <a class="abs btn" style="left:528px;top:3690px;width:144px;height:34px;font-size:13px">Join Airdrop</a>
</section>

<!-- App -->
<section>
  <div class="abs art-phone" role="img" aria-label="Smartphone showing the mascot app screen surrounded by gold GLRX coins"></div>
  <h2 class="abs app-title">Mine Directly<br>From Your Smartphone.<br>Simple, Fun, And Powerful</h2>
</section>

<!-- Presale -->
<section>
  <div class="abs glow-box" style="left:148px;top:4285px;width:903px;height:365px"></div>
  <p class="abs sec-title" style="top:4348px;font-size:38px;font-weight:400">Join the $GLRX Presale</p>
  <p class="abs sec-title" style="top:4404px;font-size:38px">Mine Crypto From Your Phone!</p>
  <p class="abs sec-title" style="top:4478px;font-size:12px;font-weight:400;line-height:18px;left:360px;width:480px">Lorem ipsum dolor sit amet, consectetur adipiscing elit, sed do eiusmod tempor incididunt ut labore et dolore magna aliqua.</p>
  <a class="abs btn" style="left:528px;top:4560px;width:144px;height:34px;font-size:13px">Join Presale</a>
</section>

<!-- Newsletter -->
<section>
  <p class="abs" style="left:152px;top:4742px;font-size:15px;font-weight:600">Sign Up for Exclusive Updates!</p>
  <div class="abs" style="left:150px;top:4817px;width:358px;height:41px;border-radius:21px;background:#3a0f8f;border:2px solid #9a4dff;display:flex;align-items:center;gap:8px;padding-left:18px;font-size:12px">
    <svg width="12" height="9" viewBox="0 0 12 9"><rect x=".5" y=".5" width="11" height="8" rx="1" fill="#fff"/><path d="M1 1l5 4 5-4" stroke="#3a0f8f" fill="none"/></svg>Email address
  </div>
  <a class="abs btn" style="left:527px;top:4818px;width:142px;height:38px;font-size:13px">Submit Now</a>

  <p class="abs" style="left:762px;top:4780px;font-size:15px;font-weight:600">Get in Touch</p>
  <div class="abs socials" style="left:762px;top:4830px;font-size:13px;gap:16px">
    <span><i></i>Chatvane</span><span><i></i>Q/Blurbly</span><span><i></i>Corvel Wallet</span>
  </div>
</section>

<!-- Footer -->
<footer>
  <a class="abs logo" style="left:150px;top:4975px;gap:14px">
    <span class="logo-dot" style="width:108px;height:108px"></span>
    <span class="logo-name"><small style="font-size:27px;font-weight:700;line-height:26px">Glintora Rex</small><b style="font-size:50px">GLRX</b></span>
  </a>
  <p class="abs" style="left:150px;top:5140px;font-size:12px">© 2025 Glintora Rex.</p>

  <div class="abs foot-col" style="left:518px;top:4950px">
    <h4>Quick Links</h4>
    <a>Home</a><a>Tokenomics</a><a>Total Supply</a><a>Roadmap</a><a>Airdrop App</a><a>Team/Founder</a><a>Contact</a>
  </div>
  <div class="abs foot-col" style="left:670px;top:4950px">
    <h4>Help Links</h4>
    <a>Terms and Conditions</a><a>Privacy Policy</a><a>Refund Policy</a><a>Disclaimer</a>
  </div>
  <div class="abs foot-col" style="left:856px;top:4950px;width:200px">
    <h4>Contact</h4>
    <div class="contact-row">
      <svg width="12" height="16" viewBox="0 0 12 16"><path d="M6 0a6 6 0 0 0-6 6c0 4.5 6 10 6 10s6-5.5 6-10a6 6 0 0 0-6-6z" fill="#fff"/><circle cx="6" cy="6" r="2.2" fill="var(--bg)"/></svg>
      <span>4120 Orbit Lane<br>Suite 210</span>
    </div>
    <div class="contact-row">
      <svg width="14" height="14" viewBox="0 0 14 14"><path d="M3 1l2 3-1.3 1.3a8 8 0 0 0 5 5L10 9l3 2-1 2.5C6 13.5.5 8 .5 2z" fill="#fff"/></svg>
      <span>+1 555-014-2290</span>
    </div>
    <div class="contact-row" style="margin-top:40px">
      <svg width="14" height="11" viewBox="0 0 14 11"><rect x=".5" y=".5" width="13" height="10" rx="1" fill="#fff"/><path d="M1 1l6 5 6-5" stroke="var(--bg)" fill="none"/></svg>
      <span>info@glintorarex.example</span>
    </div>
  </div>
  <div class="abs lang" style="left:946px;top:5186px"><i></i>English
    <svg width="9" height="6" viewBox="0 0 9 6"><path d="M1 1l3.5 3.5L8 1" stroke="#fff" fill="none" stroke-width="1.4"/></svg></div>
</footer>

</body>
</html>
```